Restaurant A5 Catering Brochure/Catalog

We are a fast casual Lebanese restaurant that needs a new multi page Catering brochure made up.

The brochure will be A5 and approx 16 pages.

We will upload media that we would like to use in the brochure in the next 24 hours.

We have uploaded the brochure brief in word file - (Brochurebrief.docx)

We have also uploaded an example of a brochure from another restaurant. it doesn't have to be similar, it just give you an idea. (brochureexample.pdf)

We have also uploaded our stylesheet. (Bramel Kitchen Style Guide.pdf)

and our logo (logo.zip)

The winner will also be able to build a similar brochure plus a function brochure for our other restaurant for additional payment.

We have uploaded many pics. In some cases multiple pictures for the same page. Feel free to choose which pic or pics to use.
Updates

ALL PHOTOS HAVE NOW BEEN UPLOADED. Some pages have multiple photos. Feel free to use any pic or pics you like. Added Wednesday, October 12, 2016

Target Market(s)

We have two target markets that we hope are looking for a different kind of catering. We offer food that is fresh, delicious, and different then traditional catering dishes like pasta or pizza.

The two markets we're after are....
1. Private catering for people looking to cater events at home like birthdays, BBQ's, etc.

2. Schools, Government Offices and Corporate Catering.

Industry/Entity Type

Restaurant

Colors
ec1f27
5c5c5c
c9c9c9
cadf82

Requirements
Must have
• Clean and visual design.
• I would prefer the design was in portrait layout like a book.

```html
<!DOCTYPE html>
<html lang="en">
<head>
<meta charset="utf-8">
<title>Catering Brochure – Vegetarian Wraps &amp; Desserts</title>
<link rel="stylesheet" href="https://fonts.googleapis.com/css2?family=Londrina+Solid:wght@400&family=Montserrat:wght@600&family=Arimo:wght@400;700&display=swap">
<style>
  :root {
    --brand-red: #ec1f27;
    --menu-red: #e0322e;
    --ink: #2b2b2b;
    --grey: #5c5c5c;
    --light-grey: #c9c9c9;
    --backdrop: #efefef;
    --paper: #ffffff;
  }
  * { box-sizing: border-box; margin: 0; padding: 0; }
  html, body { width: 1200px; height: 1000px; overflow: hidden; }
  body {
    background: var(--backdrop);
    font-family: "Arimo", Arial, sans-serif;
    color: var(--ink);
    position: relative;
  }
  .page {
    position: absolute;
    top: 183px;
    height: 630px;
    background: var(--paper);
    box-shadow: 0 1px 3px rgba(0,0,0,0.12);
  }
  .page--left { left: 180px; width: 418px; }
  .page--right { left: 598px; width: 402px; }

  .section-label {
    position: absolute;
    top: 38px; left: 0; width: 100%;
    text-align: center;
    font-size: 10px;
    color: var(--ink);
  }
  .section-label span {
    border-bottom: 1px solid var(--light-grey);
    padding-bottom: 3px;
  }
  .intro {
    position: absolute;
    top: 78px; left: 35px; width: 345px;
    font-size: 9.5px; line-height: 15px;
    color: var(--ink);
  }

  .item { position: absolute; }
  .page--left .item { left: 35px; width: 346px; }
  .page--right .item { left: 34px; width: 336px; }

  .item-head {
    display: flex; align-items: baseline;
    font-family: "Montserrat", sans-serif;
    font-weight: 600;
    font-size: 9.5px;
    letter-spacing: 0.9px;
    color: var(--menu-red);
    text-transform: uppercase;
  }
  .leader {
    flex: 1;
    margin: 0 4px;
    border-bottom: 1px dotted var(--menu-red);
    transform: translateY(-3px);
  }
  .price { letter-spacing: 0.5px; }
  .desc {
    font-size: 8px; line-height: 13px;
    color: var(--ink);
    margin-top: 3px;
  }
  .page--left .desc { margin-top: 9px; font-size: 8.5px; }

  .tier {
    display: flex; justify-content: flex-end; align-items: baseline;
    font-family: "Montserrat", sans-serif; font-weight: 600;
    font-size: 9.5px; letter-spacing: 0.9px;
    color: var(--menu-red); text-transform: uppercase;
    height: 17px;
  }
  .tier .short-leader {
    width: 24px; margin: 0 6px;
    border-bottom: 1px dotted var(--menu-red);
    transform: translateY(-3px);
  }
  .tier-row { display: flex; justify-content: space-between; align-items: baseline; }
  .tier-prices { display: flex; flex-direction: column; align-items: flex-end; }
  .desc--spaced { margin-top: 14px; text-align: justify; }

  .wrap-photo {
    position: absolute;
    top: 247px; left: 35px; width: 346px; height: 325px;
    background:
      radial-gradient(circle at 30% 40%, rgba(200,215,140,0.9), transparent 45%),
      radial-gradient(circle at 70% 70%, rgba(215,185,150,0.9), transparent 50%),
      linear-gradient(135deg, #a9b27a 0%, #6c6a4a 40%, #c8ad86 70%, #8a9a5a 100%);
  }
  .footnotes {
    position: absolute;
    top: 586px; left: 35px; width: 346px;
    font-size: 5.5px; line-height: 7px; font-weight: 700;
    color: var(--ink);
  }

  .page-title {
    position: absolute;
    top: 36px; left: 33px;
    font-family: "Londrina Solid", sans-serif;
    font-size: 19px; letter-spacing: 1.5px;
    color: var(--brand-red);
  }
</style>
</head>
<body>

  <section class="page page--left">
    <h2 class="section-label"><span>Vegetarian Wraps</span></h2>
    <p class="intro">Our Shawarma meat is whole seasoned slices of lamb or chicken roasted on a spit and sliced to order</p>

    <article class="item" style="top:128px">
      <div class="item-head"><span>Falafel Wraps</span><span class="leader"></span><span class="price">$60</span></div>
      <p class="desc">Golden brown falafel with Lettuce, tomato, onion, parsley, mixed pickles &amp; tahini sauce</p>
    </article>

    <article class="item" style="top:181px">
      <div class="item-head"><span>Grilled Veg Wrap</span><span class="leader"></span><span class="price">$60</span></div>
      <p class="desc">Lettuce, tomato, grilled onion, grilled zucchini, grilled capsicum, grilled eggplant and our Lemon Herb Mayo or Tahini sauce</p>
    </article>

    <div class="wrap-photo" role="img" aria-label="Platter of halved shawarma and falafel wraps filled with lettuce, meat and pickled turnip"></div>

    <p class="footnotes">*Wholemeal available upon request<br>*Wraps Page should have on the bottom: All platters serve 10 people and consist of 21 pieces. Each piece is approximately 1/3 of a wrap</p>
  </section>

  <section class="page page--right">
    <h1 class="page-title">DESSERTS</h1>

    <article class="item" style="top:79px">
      <div class="item-head"><span>Traditional Walnut Baklava</span><span class="leader"></span><span class="price">$20</span></div>
      <p class="desc">A sweet pastry made of layers of filo filled with chopped walnuts and sweetened and held together with our rosewater syrup.</p>
    </article>

    <article class="item" style="top:133px">
      <div class="item-head"><span>Baklava Fingers</span><span class="leader"></span><span class="price">$18</span></div>
      <p class="desc">Filo rolled and filled with chopped cashews and sweetened and held together with our rosewater syrup.</p>
    </article>

    <article class="item" style="top:187px">
      <div class="item-head"><span>Ma'amoul</span><span class="leader"></span><span class="price">$20</span></div>
      <p class="desc">Shortbread pastries either plain and filled with dates or topped with icing sugar and filled with pistachio.</p>
    </article>

    <article class="item" style="top:240px">
      <div class="item-head"><span>Namoura</span><span class="leader"></span><span class="price">$12</span></div>
      <p class="desc">Rich and dense semolina cake that crumbles in your mouth.</p>
    </article>

    <article class="item" style="top:280px">
      <div class="item-head"><span>Turkish Delights (Rahat Lakum) (12pcs)</span><span class="leader"></span><span class="price">$15</span></div>
      <p class="desc">Small cubes of fragrant jelly flavoured with Rosewater or lemon.</p>
    </article>

    <article class="item" style="top:321px">
      <div class="tier-row">
        <div class="item-head"><span>Lebanese Nights (Layali Libnan)</span></div>
        <div class="tier-prices">
          <div class="tier"><span>Tray</span><span class="short-leader"></span><span>$28</span></div>
          <div class="tier"><span>Individual</span><span class="short-leader"></span><span>$4</span></div>
        </div>
      </div>
      <p class="desc desc--spaced">An amazingly aromatic dessert that is quite refreshing. It has a rich complex taste stemming from subtle hints of mastic, orange blossom water and rose water. The bottom layer is made of pudding, topped with a layer of homemade cream and a layer of coarsely ground fresh pistachios and sugar syrup.</p>
    </article>

    <article class="item" style="top:428px">
      <div class="tier-row">
        <div class="item-head"><span>Lebanese Custard</span></div>
        <div class="tier-prices">
          <div class="tier"><span>Tray</span><span class="short-leader"></span><span>$28</span></div>
          <div class="tier"><span>Individual</span><span class="short-leader"></span><span>$4</span></div>
        </div>
      </div>
      <p class="desc desc--spaced">A layer of plain custard topped with Lebanese biscuit then topped with a layer of chocolate custard. We then put a biscuit on top.</p>
    </article>

    <article class="item" style="top:511px">
      <div class="item-head"><span>Almonds Biscuits</span><span class="leader"></span><span class="price">$12</span></div>
      <p class="desc">Our oval almond shortbread biscuits are dusted with an icing sugar.</p>
    </article>

    <article class="item" style="top:551px">
      <div class="item-head"><span>Coconut and Chocolate Chip Cookies</span><span class="leader"></span><span class="price">$15</span></div>
      <p class="desc">Soft and delicious. No further explanation needed.</p>
    </article>
  </section>

</body>
</html>
```